Brovane Grand Opening

I need a one sided flyer that advertises my grand opening for our new equipment dealership.

Grand Opening

New and Used Equipment Sales
Equipment Rentals
Residential, Commercial and Industrial Rental Equipment
Construction and Industrial Supply
Custom Metal Fabrication
Mobile Welding Service
Pickup and Delivery Service
24hr. Emergency Dedicated Service

Now Open!

4362 Marlowfield HWY
Easley, SC 29640

(555) 318 - 4026

7:00am-7:00pm Monday - Friday
8:00am-3:00pm Saturday

www.brovanegear.example

```html
<!DOCTYPE html>
<html lang="en">
<head>
<meta charset="utf-8">
<title>Brovane Grand Opening</title>
<link href="https://fonts.googleapis.com/css2?family=Anton&family=Montserrat:wght@400;500;600;700&display=swap" rel="stylesheet">
<style>
:root{
  --page:#f1f1f1;
  --ink:#2b2b2d;
  --ink-deep:#131314;
  --red:#e8202b;
  --white:#ffffff;
  --rule:#8a8a8a;
}
*{box-sizing:border-box;margin:0;padding:0}
html,body{width:1200px;height:1200px;overflow:hidden;background:var(--page)}
.flyer{position:absolute;left:205px;top:45px;width:797px;height:1118px;background:var(--ink);overflow:hidden;box-shadow:0 2px 6px rgba(0,0,0,.25);font-family:"Montserrat",sans-serif;color:var(--white)}
.hero-photo{position:absolute;left:0;top:95px;width:797px;height:850px;background:radial-gradient(ellipse at 50% 50%,#8a8780 0%,#5c5a56 35%,#2b2b2d 75%);opacity:.75}
.brand{position:absolute;top:28px;left:0;width:100%;display:flex;justify-content:center;align-items:center;gap:12px}
.brand-mark{width:30px;height:30px;background:var(--red)}
.brand-name{font-family:"Montserrat",sans-serif;font-weight:700;font-size:46px;letter-spacing:2px;color:var(--white);line-height:1}
.headline{position:absolute;left:0;width:100%;text-align:center;font-family:"Anton",sans-serif;line-height:1;transform:skewX(-6deg);text-shadow:5px 5px 0 var(--ink-deep)}
.headline-grand{top:168px;font-size:116px;color:var(--red);letter-spacing:0}
.headline-opening{top:280px;font-size:116px;color:var(--white);letter-spacing:2px}
.services{position:absolute;left:36px;top:430px;list-style:none}
.services li{display:flex;align-items:center;height:45.5px;font-size:22px;font-weight:500;letter-spacing:.3px}
.services svg{width:18px;height:18px;margin-right:19px;flex:none}
.now-open{position:absolute;top:812px;left:0;width:100%;text-align:center;font-family:"Anton",sans-serif;font-size:96px;line-height:1;transform:skewX(-6deg);text-shadow:4px 4px 0 var(--ink-deep)}
.now-open .now{color:var(--red)}
.hours{position:absolute;top:937px;left:27px;width:745px;height:27px}
.hours svg{position:absolute;inset:0}
.hours span{position:absolute;top:0;line-height:27px;font-size:20px;font-weight:700}
.hours .weekday{left:8px;color:var(--white)}
.hours .saturday{left:426px;color:var(--ink-deep)}
.footer{position:absolute;left:0;top:985px;width:797px;height:133px}
.footer svg.base{position:absolute;inset:0}
.contact{position:absolute;display:flex;align-items:center;color:var(--white)}
.contact .icon{flex:none}
.phone{left:24px;top:68px;font-size:31px;font-weight:700;gap:16px}
.web{left:465px;top:18px;font-size:19px;font-weight:500;gap:18px;white-space:nowrap}
.address{left:465px;top:48px;font-size:19px;font-weight:500;gap:18px;align-items:flex-start;line-height:26px}
</style>
</head>
<body>
<div class="flyer">
  <div class="hero-photo" role="img" aria-label="Black and white photo of a compact track loader in an equipment yard"></div>

  <div class="brand">
    <span class="brand-mark"></span>
    <span class="brand-name">BROVANE</span>
  </div>

  <div class="headline headline-grand">GRAND</div>
  <div class="headline headline-opening">OPENING</div>

  <ul class="services">
    <li><svg viewBox="0 0 20 20"><circle cx="10" cy="10" r="10" fill="#e8202b"/><path d="M5.5 10.5l3 3 6-6.5" fill="none" stroke="#fff" stroke-width="2.4" stroke-linecap="round" stroke-linejoin="round"/></svg>New and Used Equipment Sales</li>
    <li><svg viewBox="0 0 20 20"><circle cx="10" cy="10" r="10" fill="#e8202b"/><path d="M5.5 10.5l3 3 6-6.5" fill="none" stroke="#fff" stroke-width="2.4" stroke-linecap="round" stroke-linejoin="round"/></svg>Equipment Rentals</li>
    <li><svg viewBox="0 0 20 20"><circle cx="10" cy="10" r="10" fill="#e8202b"/><path d="M5.5 10.5l3 3 6-6.5" fill="none" stroke="#fff" stroke-width="2.4" stroke-linecap="round" stroke-linejoin="round"/></svg>Residential, Commercial and Industrial Rental Equipment</li>
    <li><svg viewBox="0 0 20 20"><circle cx="10" cy="10" r="10" fill="#e8202b"/><path d="M5.5 10.5l3 3 6-6.5" fill="none" stroke="#fff" stroke-width="2.4" stroke-linecap="round" stroke-linejoin="round"/></svg>Construction and Industrial Supply</li>
    <li><svg viewBox="0 0 20 20"><circle cx="10" cy="10" r="10" fill="#e8202b"/><path d="M5.5 10.5l3 3 6-6.5" fill="none" stroke="#fff" stroke-width="2.4" stroke-linecap="round" stroke-linejoin="round"/></svg>Custom Metal Fabrication</li>
    <li><svg viewBox="0 0 20 20"><circle cx="10" cy="10" r="10" fill="#e8202b"/><path d="M5.5 10.5l3 3 6-6.5" fill="none" stroke="#fff" stroke-width="2.4" stroke-linecap="round" stroke-linejoin="round"/></svg>Mobile Welding Service</li>
    <li><svg viewBox="0 0 20 20"><circle cx="10" cy="10" r="10" fill="#e8202b"/><path d="M5.5 10.5l3 3 6-6.5" fill="none" stroke="#fff" stroke-width="2.4" stroke-linecap="round" stroke-linejoin="round"/></svg>Pickup and Delivery Service</li>
    <li><svg viewBox="0 0 20 20"><circle cx="10" cy="10" r="10" fill="#e8202b"/><path d="M5.5 10.5l3 3 6-6.5" fill="none" stroke="#fff" stroke-width="2.4" stroke-linecap="round" stroke-linejoin="round"/></svg>24hr. Emergency Dedicated Service</li>
  </ul>

  <div class="now-open"><span class="now">NOW</span> OPEN!</div>

  <div class="hours">
    <svg viewBox="0 0 745 27" preserveAspectRatio="none">
      <polygon points="0,0 387,0 366,27 0,27" fill="#e8202b"/>
      <polygon points="393,0 745,0 745,27 372,27" fill="#ffffff"/>
    </svg>
    <span class="weekday">7:00am-7:00pm Monday - Friday</span>
    <span class="saturday">8:00am-3:00pm Saturday</span>
  </div>

  <div class="footer">
    <svg class="base" viewBox="0 0 797 133">
      <polyline points="0,40 412,40 449,5 797,5" fill="none" stroke="#8a8a8a" stroke-width="1.5"/>
      <polygon points="0,48 420,48 455,12 797,12 797,133 0,133" fill="#131314"/>
      <polygon points="445,12 797,12 797,133 350,133" fill="#e8202b"/>
    </svg>
    <div class="contact phone">
      <svg class="icon" width="36" height="36" viewBox="0 0 36 36"><circle cx="18" cy="18" r="16.5" fill="none" stroke="#fff" stroke-width="2"/><path d="M12.5 10.5l3 -.5 2 4.5-2 1.5c.8 2 2.5 3.7 4.5 4.5l1.5-2 4.5 2-.5 3c-6.5.5-13.5-6.5-13-13.5z" fill="none" stroke="#fff" stroke-width="1.6" stroke-linejoin="round"/></svg>
      <span>(555) 318 - 4026</span>
    </div>
    <div class="contact web">
      <svg class="icon" width="24" height="24" viewBox="0 0 24 24"><circle cx="12" cy="12" r="11" fill="none" stroke="#fff" stroke-width="1.3"/><circle cx="12" cy="12" r="6" fill="none" stroke="#fff" stroke-width="1.2"/><ellipse cx="12" cy="12" rx="2.6" ry="6" fill="none" stroke="#fff" stroke-width="1"/><path d="M6 12h12" stroke="#fff" stroke-width="1"/></svg>
      <span>www.brovanegear.example</span>
    </div>
    <div class="contact address">
      <svg class="icon" width="24" height="24" viewBox="0 0 24 24" style="margin-top:1px"><circle cx="12" cy="12" r="11" fill="none" stroke="#fff" stroke-width="1.3"/><path d="M12 17s-4-4-4-7a4 4 0 0 1 8 0c0 3-4 7-4 7z" fill="none" stroke="#fff" stroke-width="1.2"/><circle cx="12" cy="10" r="1.4" fill="#fff"/></svg>
      <span>4362 Marlowfield HWY,<br>Easley, SC 29640</span>
    </div>
  </div>
</div>
</body>
</html>
```